Harbor Crest Homes Marketing Materials
2 Pocket Folder, Wine Label, Letterhead, Biz Card
Creative Brief
Professional
Derek "Rook" Abernathy
Chief Executive Officer
4872 Pellston Ave Unit C Cedarview, MI 46719
tcalloway47@mailbryte.com
https://harborcresthomes.net/
Use the SILVER version of the logo
Logo Large in the center of black card, make it ready for foil or spot UV

```html
<!DOCTYPE html>
<html lang="en">
<head>
<meta charset="utf-8">
<title>Harbor Crest Homes – Business Card</title>
<link rel="stylesheet" href="https://fonts.googleapis.com/css2?family=Libre+Baskerville:wght@400;700&family=Arimo:wght@400&display=swap">
<style>
  :root {
    --page-bg: #2a2a2c;
    --card-dark: #333336;
    --card-darker: #242426;
    --silver: #c9cacc;
    --ink-dark: #1c1c1e;
    --text-light: #f2f2f2;
  }
  * { margin: 0; padding: 0; box-sizing: border-box; }
  html, body { width: 1200px; height: 874px; overflow: hidden; }
  body { background: var(--page-bg); position: relative; font-family: "Libre Baskerville", serif; }

  .card {
    position: absolute;
    width: 600px; height: 340px;
    border-radius: 18px;
    overflow: hidden;
    background: linear-gradient(160deg, var(--card-dark), var(--card-darker));
    box-shadow: 0 12px 30px rgba(0,0,0,0.45);
  }
  .card-front { left: 520px; top: 60px; }
  .card-back { left: 80px; top: 470px; }

  .wordmark {
    color: var(--silver);
    font-family: "Libre Baskerville", serif;
    font-weight: 700;
    text-align: center;
    line-height: 1;
  }
  .card-front .wordmark { position: absolute; left: 0; right: 0; top: 118px; }
  .wordmark .main { display: block; font-size: 50px; letter-spacing: 1px; }
  .wordmark .sub { display: block; font-size: 22px; letter-spacing: 3px; margin-top: 8px; }

  .swoosh { position: absolute; inset: 0; }

  .person { position: absolute; right: 34px; top: 62px; text-align: right; color: var(--ink-dark); }
  .person .name { font-size: 15px; font-weight: 700; letter-spacing: 0.5px; text-transform: uppercase; }
  .person .title { font-family: "Arimo", sans-serif; font-size: 12px; margin-top: 5px; }

  .card-back .wordmark { position: absolute; left: 34px; top: 220px; text-align: left; }
  .card-back .wordmark .main { font-size: 32px; letter-spacing: 0.5px; }
  .card-back .wordmark .sub { font-size: 14px; letter-spacing: 2px; margin-top: 5px; }

  .contact {
    position: absolute; right: 30px; top: 204px;
    list-style: none;
    font-family: "Arimo", sans-serif; font-size: 12.5px; color: var(--text-light);
    text-align: right; line-height: 18px;
  }
  .contact li { display: flex; justify-content: flex-end; align-items: center; gap: 8px; }
  .contact .icon { width: 11px; height: 11px; flex: none; }
  .contact .gap { margin-top: 8px; }
</style>
</head>
<body>

  <section class="card card-front" aria-label="Business card front">
    <div class="wordmark">
      <span class="main">HARBOR CREST</span>
      <span class="sub">HOMES</span>
    </div>
  </section>

  <section class="card card-back" aria-label="Business card back">
    <svg class="swoosh" viewBox="0 0 600 340" width="600" height="340" aria-hidden="true">
      <defs>
        <linearGradient id="silverBand" x1="0" y1="1" x2="1" y2="0">
          <stop offset="0" stop-color="#7d7f82"/>
          <stop offset="0.35" stop-color="#d9dadc"/>
          <stop offset="0.7" stop-color="#f3f3f4"/>
          <stop offset="1" stop-color="#b8babd"/>
        </linearGradient>
      </defs>
      <path d="M0,190 C160,120 360,30 600,0 L600,150 C430,128 220,150 0,200 Z" fill="url(#silverBand)"/>
      <path d="M0,200 C220,150 430,128 600,150" fill="none" stroke="#ffffff" stroke-opacity="0.55" stroke-width="1.5"/>
      <path d="M0,190 C160,120 360,30 600,0" fill="none" stroke="#ffffff" stroke-opacity="0.35" stroke-width="1"/>
    </svg>

    <div class="person">
      <p class="name">Derek “Rook” Abernathy</p>
      <p class="title">Chief Executive Officer</p>
    </div>

    <div class="wordmark">
      <span class="main">HARBOR CREST</span>
      <span class="sub">HOMES</span>
    </div>

    <ul class="contact">
      <li>4872 Pellston Ave Unit C</li>
      <li>Cedarview, MI 46719
        <svg class="icon" viewBox="0 0 12 12" aria-hidden="true"><path d="M6 0.5C3.8 0.5 2.2 2.1 2.2 4.2 2.2 7 6 11.5 6 11.5S9.8 7 9.8 4.2C9.8 2.1 8.2 0.5 6 0.5Z" fill="#f2f2f2"/><circle cx="6" cy="4.2" r="1.4" fill="#2a2a2c"/></svg>
      </li>
      <li class="gap">614-555-0142
        <svg class="icon" viewBox="0 0 12 12" aria-hidden="true"><path d="M2.5 0.8 4.3 0.5 5.4 3.2 4.2 4.2C4.9 5.7 6.2 7.1 7.8 7.8L8.8 6.6 11.5 7.7 11.2 9.5C10.9 10.8 9.9 11.5 8.7 11.3 4.6 10.6 1.4 7.4 0.7 3.3 0.5 2.1 1.2 1.1 2.5 0.8Z" fill="#f2f2f2"/></svg>
      </li>
      <li>tcalloway47@mailbryte.com
        <svg class="icon" viewBox="0 0 12 12" aria-hidden="true"><rect x="0.5" y="2.5" width="11" height="7.5" rx="1" fill="#f2f2f2"/><path d="M1 3 6 6.8 11 3" fill="none" stroke="#2a2a2c" stroke-width="1"/></svg>
      </li>
      <li>harborcresthomes.net
        <svg class="icon" viewBox="0 0 12 12" aria-hidden="true"><circle cx="6" cy="6" r="5" fill="none" stroke="#f2f2f2" stroke-width="1.1"/><ellipse cx="6" cy="6" rx="2.2" ry="5" fill="none" stroke="#f2f2f2" stroke-width="1"/><line x1="1" y1="6" x2="11" y2="6" stroke="#f2f2f2" stroke-width="1"/></svg>
      </li>
    </ul>
  </section>

</body>
</html>
```